Progressive business consultancy seeking "Accounting Industry Flyer"

We are looking for an industry flyer that we will use with potential clients/prospects that outlines our skills and experience in delivering change across the Accounting Services Industry. The flyer will be used to help potential clients understand the challenges and issues faced by the accounting industry and how our service offerings can help them solve their project challenges and problems.

About Us:
Based in Melbourne, Australia, Vondra-x is a management consulting organisation that partners with their clients to lead the execution of strategic process and system improvement initiatives.

Vondra-x offers business advisory services in Project Management, Business Process Management, Change Management, Business Analysis and Business Intelligence. Vondra-x combines hands on delivery with coaching in best practice methodologies and approaches to build our clients capabilities ensuring their ongoing success in project implementations.

Vondra-x has extensive experience across a wide range of industries. We specialise in assisting organisations across the accounting, legal, financial services and health sectors.

Our core purpose is to help businesses in the middle market navigate transformational change through clear and focused execution and enablement.

www.vondra-x.com.au
@vondra_x

What we're looking for:

A professional, corporate, industry flyer providing an overview of our capabilities and experience in the accounting industry. Focus is on the "e" in vondra-x. The look should be sharp and crisp, with a professional and corporate feel. The target for the flyer is Accountants and Mid-Tier Accounting Firms.

The Vondra-x colours are white and blue (RGB:0/86/162 and
CMYK 97/73/4/0)

A professional, corporate theme that is consistent across both sides of the flyer. The design should reflect our focus on the "e" in vondra-x, which is what we're really about - "e"xecution and "e"nablement of change.

I've attached a PNG file of our word template which shows the focus on the "e" as a watermark on the document as well as the font files if required.

Let me know if you need any further information or design specifics.

Thanks,

Marisol
(on behalf of Desmond)
Updates

Hi All, Thanks for your design submissions so far. We have discovered that our hero image has not been attached to the brief. Please find the jpeg attached now. It has been loaded as "Vondra-x Hero Image.jpg" Thanks Desmond @vondra_x

Reason: Hi Designers, Thanks to everyone who has taken the time to make a submission on our contest. We really appreciate it. We have decided to extend our deadline by 5 days so we can review the designs with other colleagues and provide feedback to everyone who has made a submission. Thanks for all your creative designs. Desmond @vondra_x

Reason: Hi designers, thanks to everyone for taking the time to submit their designs. We are going to have to extend our deadline again as we haven't had an opportunity to review all of the designs properly and provide feedback.

Target Market(s)

Accountants and Accounting Firms (mid tier firms)

Industry/Entity Type

Management Consulting

Font styles to use
Other font styles liked:
• Calibri & Attached font files.

Colors
0455a3
3277b5
ffffff

Requirements
Must have
• A Professional A4 double sided colour flyer consisting of:
• Front Page:
• - hero image (attached)
• - Draft content front (attached)
• - Vondra-x Logo (attached)
• Back Page
• - Draft content back (attached)

```html
<!DOCTYPE html>
<html lang="en">
<head>
<meta charset="utf-8">
<title>Vondra-x Accounting Industry Flyer</title>
<link rel="stylesheet" href="https://fonts.googleapis.com/css2?family=Archivo+Black&family=Carlito:wght@400;700&display=swap">
<style>
  :root {
    --brand-deep: #0455a3;
    --brand-mid: #3277b5;
    --brand-dark: #083a7a;
    --panel: #3c9be0;
    --white: #ffffff;
  }
  html, body { margin: 0; padding: 0; overflow: hidden; }
  body { width: 849px; height: 1200px; }
  .flyer {
    position: relative;
    width: 849px; height: 1200px; overflow: hidden;
    background: linear-gradient(160deg, #0a4f9a 0%, var(--brand-deep) 35%, #0a4a92 70%, var(--brand-dark) 100%);
    color: var(--white);
    font-family: "Carlito", "Calibri", sans-serif;
  }
  .hero-photo {
    position: absolute; left: 380px; top: 820px; width: 469px; height: 380px;
    background: radial-gradient(ellipse at 70% 55%, #e9eef4 0%, #c9d6e4 35%, rgba(150,180,215,0.55) 60%, rgba(8,58,122,0) 80%);
  }
  .main-copy {
    position: absolute; left: 40px; top: 38px; width: 480px;
    font-size: 15.2px; line-height: 19.3px;
  }
  .section-title {
    font-family: "Archivo Black", sans-serif;
    font-size: 13.4px; line-height: 16px; margin: 0 0 18px;
  }
  .main-copy p { margin: 0 0 19px; }
  .help-list { list-style: none; margin: -19px 0 19px; padding: 0; }
  .help-list li { position: relative; padding-left: 22px; }
  .help-list li::before {
    content: ""; position: absolute; left: 2px; top: 5px;
    width: 9px; height: 9px; background: var(--white);
  }
  .services {
    position: absolute; left: 535px; top: 0; width: 293px; height: 872px;
    background: var(--panel); box-sizing: border-box; padding: 36px 20px 0 20px;
  }
  .services-title {
    font-family: "Archivo Black", sans-serif; font-size: 28px; margin: 0 0 44px;
  }
  .service { margin: 0 0 24px; font-size: 18px; line-height: 24.5px; }
  .service-name { font-weight: 700; margin: 0; }
  .service-text { margin: 0; }
  .brand {
    position: absolute; left: 40px; top: 1082px;
    display: flex; align-items: flex-start; gap: 6px;
  }
  .brand-name { font-size: 76px; line-height: 76px; letter-spacing: 1px; }
  .brand-mark { width: 12px; height: 12px; border-radius: 50%; border: 1.5px solid var(--white); margin-top: 4px; }
  .brand-suffix { position: absolute; left: 285px; top: 78px; font-size: 10px; }
</style>
</head>
<body>
<div class="flyer">
  <div class="hero-photo" role="img" aria-label="Hands holding a tablet showing business charts"></div>

  <div class="main-copy">
    <h2 class="section-title">What are the major challenges facing<br>the accounting industry?</h2>
    <p>The three major disruptors facing accounting firms are the offshoring of compliance activities, rapid changes in technology and the internet. These industry wide disruptors are placing pressure on fee negotiations, revenue generation and are also providing a significant increase in competitive activity. As clients continue to push prices down, accounting firms have and/or are in the process of implementing systems and technologies to drive further efficiencies and reduce costs. In addition the outsourcing of accounting services for low end and non-confidential work to further lower client costs has been pervasive. This has now started to extend across end to end tax and audit compliance processes as firms start to recognise the qualified accounting capability they have available to them at a much lower cost.</p>
    <p>The need to win new business and increased competition has resulted in the entry of the Big 4 into the middle tier market and the emergence and expansion of non-traditional competitors with different business models. Cloud computing is enabling businesses to scale at a very rapid rate and maintain low cost operating models. As the industry becomes hyper-competitive it is crucial for accounting firms to deepen their understanding of clients and build their capability to offer value added advisory services.</p>
    <h2 class="section-title">How we can help professional services firms<br>in the accounting industry</h2>
    <p>Vondra-x have deep industry experience gained across the Big 4 and mid-tier accounting firms and a consistent track record for leading change and delivering improvements to business processes. Our people have extensive industry experience leading and managing teams at organisations such as Harrow Lane, Colbeck Morrow, Tallis Group, Renwick Accountants, Northgate Advisers and Ellery Partners.</p>
    <p>Our delivery model involves us working directly alongside you helping you to:</p>
    <ul class="help-list">
      <li>Recognise the major disruptors for your business</li>
      <li>Ensure you have developed a clear strategy on how to respond</li>
      <li>Develop a plan and execute the changes required to ensure business growth is maintained and the quality of your client work is not compromised</li>
    </ul>
    <h2 class="section-title">Case Study</h2>
    <p>A leading mid-tier accounting firm required support to implement large scale process and system improvements identified through a major organisational review. Through a structured program delivery approach we harnessed the required internal resources, engaged widely across the organisation and delivered major changes throughout the firm every 8 weeks with minimal disruption to normal business operations. The implementation of these improvements freed up over x hours per annum that could be redirected to value added advisory services.</p>
  </div>

  <aside class="services">
    <h1 class="services-title">What We Do.</h1>
    <div class="service"><p class="service-name">Project Management</p><p class="service-text">Delivering high quality<br>projects on time<br>and within budget.</p></div>
    <div class="service"><p class="service-name">Business Process Management</p><p class="service-text">Engaging your people to<br>understand current<br>practices and develop<br>smarter business processes</p></div>
    <div class="service"><p class="service-name">Change Management</p><p class="service-text">Building engagement<br>through business<br>understanding, clear<br>communication and<br>relevant capability.</p></div>
    <div class="service"><p class="service-name">Business Analysis</p><p class="service-text">Building innovative links<br>between your<br>departments, driving<br>collaboration and providing<br>holistic business solutions.</p></div>
    <div class="service"><p class="service-name">Business Intelligence</p><p class="service-text">Leveraging one of your<br>organisations most<br>valuable assets--your<br>data.</p></div>
  </aside>

  <div class="brand">
    <span class="brand-name">Vondra-x</span>
    <span class="brand-mark"></span>
    <span class="brand-suffix">Pty Ltd</span>
  </div>
</div>
</body>
</html>
```